QORVIX needs a new business card!

QORVIX is a group of gaming enthusiasts who are looking for a new corporate business card.

The typeface should be modern and minimalist with attention paid to spacing between the letters and the letters 'qorvix' look relative to each other.

Should clean, crisp and minimalist - looking serious overall but with slight tweaks to the letters to make them look playful...

Black on white is fine.

Details on the card should include:
-the word 'qorvix'
-a job title (use any, for e.g. founder)
-a name (e.g. Ned Pallister)
-phone number
-email address

For inspiration: http://brevant.tamblework-cdn.example/wp-content/uploads/2013/07/kelo-1.jpg

Target Market(s)

Video gaming enthusiasts

Industry/Entity Type

Business

Requirements
Must have
• Black letter on white background.
The word "qorvix"
Nice to have
• Maybe use a conservative font like Gibraltar or Helvetica and tweaking each letter individually.

You can insert normal job titles under the "qorvix" typeface
Should not have
• Should not be cartoony or childish fonts. No colors.

```html
<!DOCTYPE html>
<html lang="en">
<head>
<meta charset="utf-8">
<title>QORVIX Business Card</title>
<link rel="stylesheet" href="https://fonts.googleapis.com/css2?family=Fira+Sans:wght@300;400;500;800&display=swap">
<style>
  :root {
    --stage: #e4e4e6;
    --card: #ffffff;
    --ink: #111111;
    --muted: #8a8a8a;
    --shadow: rgba(0, 0, 0, 0.18);
  }
  * { box-sizing: border-box; margin: 0; padding: 0; }
  html, body {
    width: 1200px;
    height: 1000px;
    overflow: hidden;
    background: var(--stage);
  }
  .stage {
    position: relative;
    width: 1200px;
    height: 1000px;
  }
  .card {
    position: absolute;
    left: 150px;
    top: 243px;
    width: 900px;
    height: 514px;
    background: var(--card);
    box-shadow: 0 10px 30px var(--shadow);
    font-family: "Fira Sans", sans-serif;
    color: var(--ink);
  }
  .wordmark {
    position: absolute;
    left: 0;
    right: 0;
    top: 130px;
    text-align: center;
    font-weight: 800;
    font-size: 128px;
    letter-spacing: 6px;
    line-height: 1;
    color: var(--ink);
  }
  .tagline {
    position: absolute;
    left: 0;
    right: 0;
    top: 300px;
    text-align: center;
    font-weight: 300;
    font-size: 22px;
    letter-spacing: 11px;
    color: var(--muted);
  }
  .contact-row {
    position: absolute;
    left: 0;
    right: 0;
    bottom: 68px;
    display: flex;
    justify-content: center;
    align-items: baseline;
    gap: 22px;
    font-size: 20px;
    letter-spacing: 1px;
  }
  .contact-name { font-weight: 500; font-size: 23px; }
  .contact-title { font-weight: 400; font-size: 17px; margin-left: -12px; }
  .contact-item { display: inline-flex; align-items: center; gap: 10px; font-weight: 400; }
  .contact-icon { width: 20px; height: 20px; fill: var(--ink); align-self: center; }
</style>
</head>
<body>
<main class="stage">
  <section class="card" aria-label="QORVIX business card">
    <h1 class="wordmark">QORVIX</h1>
    <p class="tagline">GAMING ENTHUSIASTS</p>
    <div class="contact-row">
      <span class="contact-name">TOMAS REYLE</span>
      <span class="contact-title">MANAGER</span>
      <span class="contact-item">
        <svg class="contact-icon" viewBox="0 0 24 24" aria-hidden="true">
          <path d="M6.6 2.5c.6-.3 1.3-.1 1.6.5l2 3.6c.3.6.2 1.2-.3 1.6l-1.6 1.3c1 2.2 2.8 4 5 5l1.3-1.6c.4-.5 1-.6 1.6-.3l3.6 2c.6.3.8 1 .5 1.6l-1.2 2.6c-.4.8-1.3 1.2-2.2 1C10 18.5 5.5 14 4.2 7.3c-.2-.9.2-1.8 1-2.2z"/>
        </svg>
        011-402-58-316900
      </span>
      <span class="contact-item">
        <svg class="contact-icon" viewBox="0 0 24 24" aria-hidden="true">
          <path d="M2 5h20v2l-10 6L2 7z"/>
          <path d="M2 9l10 6 10-6v10H2z"/>
        </svg>
        HELLO@QORVIX.NET
      </span>
    </div>
  </section>
</main>
</body>
</html>
```